Driftwood Coatings of Central Florida, LLC. Start-up painting business needs a professional web desig

We have a start up painting business that would like to reach/focus on commercial clients like building contractors, HOA's, apartment complexes, etc.. We would like a residential aspect to the web design as well. We have an existing website at "trydriftwoodcoatings.com" with usable content. Have logo and color scheme attached. Use provided website ONLY as template. Add commercial services page. Can type own content when needed.

```html
<!DOCTYPE html>
<html lang="en">
<head>
<meta charset="utf-8">
<title>Driftwood Coatings</title>
<link href="https://fonts.googleapis.com/css2?family=Roboto:wght@400;500;700&display=swap" rel="stylesheet">
<style>
:root{
  --salmon:#e8a48c;
  --salmon-dark:#d98e74;
  --rust:#b9583f;
  --rust-text:#c0573c;
  --orange:#f5a40b;
  --orange-dark:#9a5a06;
  --ink:#4a4a4a;
  --grey:#777;
  --line:#dcdcdc;
  --white:#fff;
}
*{margin:0;padding:0;box-sizing:border-box}
html,body{width:1200px;height:2195px;overflow:hidden;background:var(--white);font-family:"Roboto",sans-serif;color:var(--ink)}
.page{position:relative;width:1200px;height:2195px}
.abs{position:absolute}

.topbar{left:0;top:0;width:1200px;height:98px;background:var(--salmon)}
.brand{left:88px;top:0;width:239px;height:139px;background:var(--white);box-shadow:0 3px 8px rgba(0,0,0,.25);display:flex;align-items:flex-end;justify-content:center;padding-bottom:22px}
.brand-name{font-size:24px;font-weight:700;color:var(--rust-text);letter-spacing:.5px;white-space:nowrap}
.nav-active{left:434px;top:0;width:70px;height:98px;background:var(--salmon-dark)}
.nav-link{top:40px;transform:translateX(-50%);color:var(--white);font-size:14px;white-space:nowrap}
.social-top{left:1025px;top:132px;display:flex;gap:22px}
.social-top span{width:14px;height:14px;border-radius:50%;background:var(--salmon)}

.hero{left:88px;top:185px;width:1027px;height:430px;background:linear-gradient(90deg,#dfe7ea 0%,#8fe0e0 35%,#6ed9dc 60%,#e9eef0 100%);box-shadow:0 8px 12px -6px rgba(0,0,0,.35)}
.hero-copy{left:264px;top:348px;width:480px}
.hero-copy h1{font-size:29px;font-weight:700;color:#1c4e55;margin-bottom:8px;white-space:nowrap}
.hero-copy p{width:420px;font-size:12.5px;line-height:19px;color:#1c4e55}
.dots{left:563px;top:626px;display:flex;gap:8px}
.dots span{width:8px;height:8px;border-radius:50%;background:var(--salmon)}

.title{left:0;width:1200px;text-align:center;font-size:23px;font-weight:500;color:var(--rust-text)}
.swoosh{left:555px;width:90px;height:10px}
.welcome-text{left:88px;top:745px;width:1027px;text-align:center;font-size:11.5px;line-height:19px;color:var(--grey)}

.service{top:830px;width:246px;height:360px}
.service svg.bg{position:absolute;left:0;top:0}
.service .icon{position:absolute;left:88px;top:58px}
.service h3{position:absolute;left:0;top:147px;width:100%;text-align:center;color:var(--white);font-size:18px;font-weight:700;white-space:nowrap}
.service p{position:absolute;left:18px;top:183px;width:210px;text-align:center;color:var(--white);font-size:11.5px;line-height:18px}
.service .more{position:absolute;left:79px;top:256px;width:88px;height:30px;background:var(--orange-dark);color:var(--white);font-size:14px;display:flex;align-items:center;justify-content:center}

.comm{top:1318px;width:246px;height:228px;border:1px solid var(--line)}
.comm .photo{width:236px;height:110px;margin:5px 5px 0}
.comm h4{font-size:17px;font-weight:400;color:var(--rust-text);margin:14px 0 6px 6px}
.comm p{font-size:12px;line-height:16px;color:var(--grey);margin:0 6px;height:32px;overflow:hidden}
.comm .row{position:absolute;left:0;bottom:0;width:100%;height:28px;border-top:1px solid var(--line);display:flex;align-items:center;justify-content:space-between;padding-left:6px;font-size:12px;color:var(--rust-text)}
.comm .row span.arrow{width:28px;height:28px;border-left:1px solid var(--line);display:flex;align-items:center;justify-content:center;color:var(--grey)}

.painter{left:88px;top:1586px;width:262px;height:342px;background:linear-gradient(180deg,#f4f4f4,#e3e6e8 70%,#f7f7f7)}
.include{left:422px;top:1592px;width:690px}
.include h2{font-size:18px;font-weight:500;color:var(--rust-text);margin-bottom:14px}
.include p{font-size:12px;line-height:21px;color:var(--grey);margin-bottom:12px}
.include ul{list-style:none}
.include li{display:flex;align-items:center;gap:10px;font-size:13px;color:var(--grey);height:34px}
.quote{display:inline-block;margin-top:10px;background:var(--rust);color:var(--white);font-size:13px;padding:7px 9px;border-radius:3px}

.footer{left:0;top:1967px;width:1200px;height:144px;background:var(--rust)}
.notch{left:638px;top:1967px}
.contact{top:2018px;display:flex;align-items:center;gap:16px;color:var(--white);white-space:nowrap}
.contact .circle{width:48px;height:48px;border-radius:50%;background:var(--white);display:flex;align-items:center;justify-content:center}
.find{left:815px;top:2025px;display:flex;align-items:center;gap:10px;color:var(--white);font-size:24px;white-space:nowrap}
.find span.c{width:38px;height:38px;border-radius:50%;background:var(--white)}
.bottom{left:88px;top:2140px;width:1027px;display:flex;justify-content:space-between;font-size:13px;color:var(--rust-text)}
.bottom nav{display:flex;gap:26px}
</style>
</head>
<body>
<div class="page">
  <div class="abs topbar"></div>
  <div class="abs nav-active"></div>
  <span class="abs nav-link" style="left:469px">Home</span>
  <span class="abs nav-link" style="left:573px">About Us</span>
  <span class="abs nav-link" style="left:725px">Commercial Services</span>
  <span class="abs nav-link" style="left:876px">Products</span>
  <span class="abs nav-link" style="left:976px">Blog</span>
  <span class="abs nav-link" style="left:1081px">Contact Us</span>
  <div class="abs brand"><span class="brand-name">Driftwood Coatings</span></div>
  <div class="abs social-top"><span></span><span></span><span></span></div>

  <div class="abs hero" role="img" aria-label="Photo of a painter rolling turquoise paint onto a white wall beside a ladder"></div>
  <div class="abs hero-copy">
    <h1>WHERE DREAMS MEET REALITY</h1>
    <p>Lorem Ipsum is simply dummy text of the printing and typesetting industry. Lorem Ipsum has been the industry's standard dummy text ever since the 1500s, when an unknown printer took a galley of type and scrambled</p>
  </div>
  <div class="abs dots"><span></span><span></span><span></span></div>

  <h2 class="abs title" style="top:690px">Welcome to Driftwood Coatings</h2>
  <svg class="abs swoosh" style="top:722px" viewBox="0 0 90 10"><path d="M2 8 Q45 -2 88 8" stroke="#c0573c" stroke-width="3" fill="none"/></svg>
  <p class="abs welcome-text">Contrary to popular belief, Lorem Ipsum is not simply random text. It has roots in a piece of classical Latin literature from 45 BC, making it over 2000 years old. Dana Whitfield, a Latin professor at Ashgrove Hill College in Vermont, looked up one of the more obscure Latin words, consectetur</p>

  <div class="abs service" style="left:88px">
    <svg class="bg" width="246" height="360" viewBox="0 0 246 360"><path d="M0 10 L20 4 L45 12 L70 2 L100 10 L130 0 L160 9 L190 3 L220 11 L246 2 L246 312 L123 360 L0 312 Z" fill="#f5a40b"/></svg>
    <svg class="icon" width="70" height="70" viewBox="0 0 70 70"><g stroke="#7a4700" stroke-width="7" stroke-linecap="round"><line x1="10" y1="60" x2="58" y2="12"/><line x1="12" y1="12" x2="60" y2="60"/></g></svg>
    <h3>Repair Services</h3>
    <p>The standard chunk of Lorem Ipsum used since the 1500s is reproduced below for those interested. Sections</p>
    <div class="more">More</div>
  </div>
  <div class="abs service" style="left:349px">
    <svg class="bg" width="246" height="360" viewBox="0 0 246 360"><path d="M0 6 L30 12 L60 2 L90 10 L120 3 L150 12 L180 4 L210 10 L246 3 L246 312 L123 360 L0 312 Z" fill="#f5a40b"/></svg>
    <svg class="icon" width="70" height="70" viewBox="0 0 70 70"><g stroke="#7a4700" stroke-width="5" fill="none" stroke-linejoin="round"><path d="M8 32 L35 8 L62 32 L62 62 L8 62 Z"/><rect x="20" y="38" width="30" height="14"/></g></svg>
    <h3>Interior Design Services</h3>
    <p>The standard chunk of Lorem Ipsum used since the 1500s is reproduced below for those interested. Sections</p>
    <div class="more">More</div>
  </div>
  <div class="abs service" style="left:610px">
    <svg class="bg" width="246" height="360" viewBox="0 0 246 360"><path d="M0 4 L25 11 L55 3 L85 12 L115 2 L145 10 L175 3 L205 12 L246 4 L246 312 L123 360 L0 312 Z" fill="#f5a40b"/></svg>
    <svg class="icon" width="70" height="70" viewBox="0 0 70 70"><g fill="#7a4700"><path d="M40 6 L64 30 L48 40 L30 22 Z"/><path d="M30 30 L40 40 L16 66 L6 62 L4 56 Z"/></g></svg>
    <h3>Interior Painting Services</h3>
    <p>The standard chunk of Lorem Ipsum used since the 1500s is reproduced below for those interested. Sections</p>
    <div class="more">More</div>
  </div>
  <div class="abs service" style="left:870px">
    <svg class="bg" width="246" height="360" viewBox="0 0 246 360"><path d="M0 9 L30 2 L60 11 L90 4 L120 12 L150 2 L180 10 L215 3 L246 10 L246 312 L123 360 L0 312 Z" fill="#f5a40b"/></svg>
    <svg class="icon" width="70" height="70" viewBox="0 0 70 70"><g fill="#7a4700"><rect x="14" y="4" width="44" height="16" rx="3"/><path d="M58 12 L64 12 L64 30 L36 30 L36 38 L32 38 L32 26 L60 26 L60 16 Z"/><rect x="29" y="38" width="10" height="28" rx="3"/></g></svg>
    <h3>Exterior Painting Services</h3>
    <p>The standard chunk of Lorem Ipsum used since the 1500s is reproduced below for those interested. Sections</p>
    <div class="more">More</div>
  </div>

  <h2 class="abs title" style="top:1226px">Our Commercial Services</h2>
  <svg class="abs swoosh" style="top:1259px" viewBox="0 0 90 10"><path d="M2 8 Q45 -2 88 8" stroke="#c0573c" stroke-width="3" fill="none"/></svg>

  <div class="abs comm" style="left:88px">
    <div class="photo" role="img" aria-label="Photo of building contractors on a construction site" style="background:linear-gradient(135deg,#8a7a6a,#c9c3bb 60%,#6e6a60)"></div>
    <h4>Building Contractors</h4>
    <p>Contrary to popular belief, Lorem Ipsum is not simply random text. It has roots in a</p>
    <div class="row">Read More<span class="arrow">›</span></div>
  </div>
  <div class="abs comm" style="left:349px">
    <div class="photo" role="img" aria-label="Photo of a family in front of a suburban home" style="background:linear-gradient(135deg,#6f8f6a,#b8c3c9 55%,#8d6b5a)"></div>
    <h4>HOA</h4>
    <p>Contrary to popular belief, Lorem Ipsum is not simply random text. It has roots in a</p>
    <div class="row">Read More<span class="arrow">›</span></div>
  </div>
  <div class="abs comm" style="left:610px">
    <div class="photo" role="img" aria-label="Photo of a row of brick apartment buildings" style="background:linear-gradient(180deg,#c5d6e2,#9b5a45 55%,#6f7a5a)"></div>
    <h4>Apartment Complexes</h4>
    <p>Contrary to popular belief, Lorem Ipsum is not simply random text. It has roots in a</p>
    <div class="row">Read More<span class="arrow">›</span></div>
  </div>
  <div class="abs comm" style="left:870px">
    <div class="photo" role="img" aria-label="Photo of a paint roller on a wall" style="background:linear-gradient(135deg,#d9d2c8,#a89a88 60%,#eae6e0)"></div>
    <h4>Lorem Ipsum Dollar</h4>
    <p>Contrary to popular belief, Lorem Ipsum is not simply random text. It has roots in a</p>
    <div class="row">Read More<span class="arrow">›</span></div>
  </div>

  <div class="abs painter" role="img" aria-label="Photo of a painter in white overalls on a step ladder with a roller"></div>
  <div class="abs include">
    <h2>Our Painting Service Include</h2>
    <p>The standard chunk of Lorem Ipsum used since the 1500s is reproduced below for those interested. Sections 1.10.32 and 1.10.33 from an old Latin treatise on ethics are also reproduced in their exact original form, accompanied by English versions from a later translation by M. Hollis.</p>
    <ul>
      <li><svg width="14" height="14" viewBox="0 0 14 14"><circle cx="7" cy="7" r="6" fill="none" stroke="#777" stroke-width="1.5"/><path d="M4 7 L6.3 9.2 L10 5" stroke="#777" stroke-width="1.5" fill="none"/></svg>Contrary to popular belief, Lorem Ipsum</li>
      <li><svg width="14" height="14" viewBox="0 0 14 14"><circle cx="7" cy="7" r="6" fill="none" stroke="#777" stroke-width="1.5"/><path d="M4 7 L6.3 9.2 L10 5" stroke="#777" stroke-width="1.5" fill="none"/></svg>Contrary to popular belief, Lorem Ipsum</li>
      <li><svg width="14" height="14" viewBox="0 0 14 14"><circle cx="7" cy="7" r="6" fill="none" stroke="#777" stroke-width="1.5"/><path d="M4 7 L6.3 9.2 L10 5" stroke="#777" stroke-width="1.5" fill="none"/></svg>Contrary to popular belief, Lorem Ipsum</li>
      <li><svg width="14" height="14" viewBox="0 0 14 14"><circle cx="7" cy="7" r="6" fill="none" stroke="#777" stroke-width="1.5"/><path d="M4 7 L6.3 9.2 L10 5" stroke="#777" stroke-width="1.5" fill="none"/></svg>Contrary to popular belief, Lorem Ipsum</li>
      <li><svg width="14" height="14" viewBox="0 0 14 14"><circle cx="7" cy="7" r="6" fill="none" stroke="#777" stroke-width="1.5"/><path d="M4 7 L6.3 9.2 L10 5" stroke="#777" stroke-width="1.5" fill="none"/></svg>Contrary to popular belief, Lorem Ipsum</li>
    </ul>
    <span class="quote">Get a Free Quote</span>
  </div>

  <div class="abs footer"></div>
  <svg class="abs notch" width="44" height="20" viewBox="0 0 44 20"><path d="M0 0 L44 0 L22 20 Z" fill="#fff"/></svg>
  <div class="abs contact" style="left:88px;font-size:23px">
    <span class="circle"><svg width="24" height="24" viewBox="0 0 24 24"><path d="M6 2 L10 6 L8 9 Q10 14 15 16 L18 14 L22 18 L19 22 Q6 20 2 5 Z" fill="#b9583f"/></svg></span>503-555-0186
  </div>
  <div class="abs contact" style="left:428px;font-size:15px">
    <span class="circle"><svg width="24" height="18" viewBox="0 0 24 18"><rect x="1" y="1" width="22" height="16" rx="2" fill="#b9583f"/><path d="M2 2 L12 10 L22 2" stroke="#fff" stroke-width="2" fill="none"/></svg></span>hello@driftwoodcoatings.net
  </div>
  <div class="abs find">Find us on :<span class="c"></span><span class="c"></span><span class="c"></span><span class="c"></span></div>

  <div class="abs bottom">
    <nav><span>Home</span><span>About Us</span><span>Commercial Services</span><span>Products</span><span>Blog</span></nav>
    <span>© 2015 Driftwoodcoatings.com. All Rights Reserved.</span>
  </div>
</div>
</body>
</html>
```